yourSmileCare Brookvale Business Card

Please design a two sided business card that is Elegant and Professional
Add subtle elegant patterns to suit Spot UV printing/ or raised printing

Name: Dr Marcus T. Fenwick
Qualification: BDSc (QLD)
Title: Dental Surgeon, Clinical Director
Company: yourSmileCare Brookvale
Phone: (02) 7593 2268
Address: Shop 7/18-20 Lindon Ave Brookvale 2097
email: info@yoursmilecarebrookvale.com.au
Facebook: facebook.com/yoursmilecarebrookvale

Motto:
Quality dentistry you can trust

Description of services (not compulsory):
Preventative Dentistry | General Dentistry
Cosmetic Dentistry | Teeth Whitening
Crown and Bridge | Root Canal Therapy
Veneers | Clearvono | Orthodontics
Emergency Dental Care | After Hours

Personalised Treatment Plans
Transparent Fees

Please make sure card is elegant and professional

Target Market(s)

general population, patients,
Dental sales companies, other professions

Industry/Entity Type

Dental Clinic

Contact Information for Business Card

Name: Dr Marcus T. Fenwick
Qualification: BDSc (QLD)
Phone: (02) 7593 2268
Address: Shop 7/18-20 Lindon Ave Brookvale

Motto:

Description of services (not compulsory)

Transparent Fees

Image of dental surgery optional

Please make sure card is elegant and profession

Requirements
Must have
• Logo
• Name, Title (next to name), Business
• Phone, address, facbeook
• Must have stylish design to suit SPOT UV reflective printing
Nice to have
• Subtle elegant patterns which will have Spot UV on them when printed
• Colours to match logo colour
• Description of services
Should not have
• Small fonts that are hard to read
• DO NOT PUT IMAGES OF DENTAL INSTRUMENTS OR TEETH PLEASE

```html
<!DOCTYPE html>
<html lang="en">
<head>
<meta charset="utf-8">
<title>yourSmileCare Brookvale Business Card</title>
<link rel="stylesheet" href="https://fonts.googleapis.com/css2?family=Open+Sans:wght@400;600;700&display=swap">
<style>
  :root {
    --page-bg: #e9e7e3;
    --green: #7dbb2f;
    --green-light: #a9d65a;
    --green-dark: #5f9a1e;
    --grey: #6d6e71;
    --grey-light: #b5b6b8;
    --charcoal: #4a4b4e;
    --charcoal-dark: #3a3b3d;
    --white: #ffffff;
    --card-w: 760px;
    --card-h: 434px;
  }
  * { box-sizing: border-box; margin: 0; padding: 0; }
  html, body {
    width: 1200px; height: 950px; overflow: hidden;
    background: var(--page-bg);
    font-family: "Open Sans", Arial, sans-serif;
  }
  .sheet {
    width: 1200px; height: 950px;
    display: flex; flex-direction: column; align-items: center; justify-content: center;
    gap: 36px;
  }
  .card {
    position: relative;
    width: var(--card-w); height: var(--card-h);
    border-radius: 26px; overflow: hidden;
    box-shadow: 0 6px 18px rgba(0,0,0,0.18);
  }
  .card-art { position: absolute; inset: 0; width: 100%; height: 100%; }

  /* Front */
  .brand {
    position: absolute; left: 34px; top: 150px;
    display: flex; align-items: center; gap: 12px;
  }
  .brand-dot { width: 22px; height: 22px; border-radius: 50%; background: var(--green); flex: none; }
  .brand-name {
    color: var(--grey); font-weight: 700; font-size: 29px; line-height: 1.1;
  }
  .contact {
    position: absolute; right: 38px; top: 52px;
    text-align: right; color: var(--white);
  }
  .contact-name { font-size: 25px; font-weight: 700; line-height: 1.2; }
  .contact-name .qual { font-size: 17px; font-weight: 600; }
  .contact-title { font-size: 17px; margin-bottom: 34px; }
  .contact-line {
    font-size: 17px; line-height: 1.55;
    display: flex; justify-content: flex-end; align-items: center; gap: 10px;
  }
  .contact-line svg { width: 20px; height: 20px; flex: none; }
  .address { margin-bottom: 6px; }
  .motto-front { font-size: 17px; font-weight: 600; margin-top: 4px; }

  /* Back */
  .back { background: linear-gradient(160deg, #6b6c6f 0%, var(--charcoal) 55%, var(--charcoal-dark) 100%); }
  .back-brand {
    position: absolute; left: 0; right: 0; top: 70px;
    display: flex; justify-content: center; align-items: center; gap: 16px;
  }
  .back-brand .brand-dot { width: 34px; height: 34px; }
  .back-brand .brand-name { color: #e6e6e6; font-size: 44px; }
  .motto-back {
    position: absolute; left: 0; right: 0; top: 176px;
    text-align: center; color: var(--green-light); font-weight: 700; font-size: 21px;
  }
  .services {
    position: absolute; left: 0; right: 0; top: 222px;
    text-align: center; color: #e3e3e3; font-size: 17px; line-height: 1.6;
    list-style: none;
  }
  .services-band {
    position: absolute; left: 0; right: 0; bottom: 0; height: 56px;
    background: linear-gradient(90deg, var(--green-dark), var(--green), var(--green-light));
    color: var(--white); font-size: 17px; font-weight: 600;
    display: flex; align-items: center; justify-content: center;
  }
</style>
</head>
<body>
<main class="sheet">

  <section class="card back" aria-label="Card back">
    <div class="back-brand">
      <span class="brand-dot"></span>
      <span class="brand-name">yourSmileCare Brookvale</span>
    </div>
    <p class="motto-back">Quality dentistry you can trust</p>
    <ul class="services">
      <li>Preventative Dentistry | General Dentistry | Cosmetic Dentistry</li>
      <li>Teeth Whitening | Crown and Bridge | Root Canal Therapy | Veneers</li>
      <li>Clearvono | Orthodontics | Emergency Dental Care | After Hours</li>
    </ul>
    <div class="services-band">Personalised Treatment Plans | Transparent Fees</div>
  </section>

  <section class="card front" aria-label="Card front">
    <svg class="card-art" viewBox="0 0 760 434" preserveAspectRatio="none" aria-hidden="true">
      <defs>
        <linearGradient id="greenFill" x1="0" y1="0" x2="1" y2="1">
          <stop offset="0" stop-color="#b4dc68"/>
          <stop offset="0.5" stop-color="#8cc63f"/>
          <stop offset="1" stop-color="#6aa823"/>
        </linearGradient>
        <linearGradient id="greyFill" x1="0" y1="0" x2="0" y2="1">
          <stop offset="0" stop-color="#9a9b9e"/>
          <stop offset="1" stop-color="#6d6e71"/>
        </linearGradient>
      </defs>
      <rect width="760" height="434" fill="url(#greenFill)"/>
      <path d="M0 0 H330 C390 40 355 140 365 210 C375 300 300 380 345 434 H0 Z" fill="url(#greyFill)"/>
      <path d="M0 0 H300 C355 40 325 140 335 210 C345 300 270 380 315 434 H0 Z" fill="#ffffff"/>
      <path d="M300 0 C355 40 325 140 335 210 C345 300 270 380 315 434" fill="none" stroke="#ffffff" stroke-width="3" transform="translate(16 0)"/>
    </svg>

    <div class="brand">
      <span class="brand-dot"></span>
      <span class="brand-name">yourSmileCare<br>Brookvale</span>
    </div>

    <div class="contact">
      <p class="contact-name">Dr Marcus T. Fenwick <span class="qual">BDSc (QLD)</span></p>
      <p class="contact-title">Dental Surgeon, Clinical Director</p>
      <p class="contact-line address">Shop 7/18-20<br>Lindon Ave Brookvale</p>
      <p class="contact-line">(02) 7593 2268
        <svg viewBox="0 0 24 24" aria-hidden="true"><path fill="#fff" d="M4 9c0-3 3-5 8-5s8 2 8 5l-4 1-1-2H9l-1 2-4-1zm3 3h10l2 7H5z"/></svg>
      </p>
      <p class="contact-line">info@yoursmilecarebrookvale.com.au
        <svg viewBox="0 0 24 24" aria-hidden="true"><rect x="3" y="6" width="18" height="12" rx="1.5" fill="#fff"/><path d="M3.5 7l8.5 6 8.5-6" fill="none" stroke="#7dbb2f" stroke-width="1.6"/></svg>
      </p>
      <p class="contact-line">/yoursmilecarebrookvale
        <svg viewBox="0 0 24 24" aria-hidden="true"><rect x="4" y="4" width="16" height="16" rx="2" fill="#fff"/></svg>
      </p>
      <p class="motto-front">Quality dentistry you can trust</p>
    </div>
  </section>

</main>
</body>
</html>
```